Fleur Vallon Riding School Flyer Design

We need a flyer for our Horse riding school, called Fleur Vallon Riding School.

At Fleur Vallon Riding School, Horses and ponies are carefully matched to suit each rider's experience, ability and confidence. I am a Qualified instructor, equipped to train all levels from nervous beginners to the more advanced.

Horse riding is fun! Riders, particularly children, are taught not only skills on the horse, but skills that are integral to good horsemanship and ownership of horses.

We regularly host Ladies Days, Guest Instructors, 1 hour Trail Rides and Pony Ride Days!

We teach people how to interact safely with, and care for horses so they develop a genuine love and respect for the animals and the sport.

In addition to fundamental riding techniques including walk, trot, and canter, we teach our students:
Grooming and Care of horses, Safety around horses, Balance and Co-Ordination, How to saddle up and care for Tack, Responsibility for equipment and horse, Confidence and Confidence Building for all Ages.

Private and group lessons start at 5 years of age upwards.

We recommend children 4 years and under partake in 15 minute pony rides, mainly due to their attention span!

```html
<!DOCTYPE html>
<html lang="en">
<head>
<meta charset="utf-8">
<title>Fleur Vallon Riding School Flyer</title>
<link href="https://fonts.googleapis.com/css2?family=Arimo:wght@400;700&family=Kalam:wght@400;700&display=swap" rel="stylesheet">
<style>
  :root {
    --page-bg: #e6e6e6;
    --forest: #3d4a3e;
    --lime: #c6d631;
    --white: #ffffff;
    --panel-tint: rgba(72, 82, 62, 0.62);
    --photo-dark: #3a2e26;
    --photo-mid: #6b5a4a;
    --photo-light: #8d9478;
  }
  * { margin: 0; padding: 0; box-sizing: border-box; }
  html, body { width: 1200px; height: 1000px; overflow: hidden; }
  body { background: var(--page-bg); font-family: "Arimo", Arial, sans-serif; position: relative; }

  .flyer {
    position: absolute; left: 93px; top: 120px;
    width: 1020px; height: 722px; overflow: hidden;
    background: var(--forest);
  }
  .stable-photo {
    position: absolute; left: 0; top: 0; width: 1020px; height: 520px;
    background:
      linear-gradient(90deg, var(--photo-dark) 0%, #5a4434 22%, var(--photo-mid) 38%, #4b3f35 50%, var(--photo-light) 75%, #9aa284 100%);
  }
  .info-panel {
    position: absolute; left: 512px; top: 0; width: 508px; height: 520px;
    background: var(--panel-tint);
  }
  .wave { position: absolute; left: 0; top: 0; width: 1020px; height: 722px; }

  .info-copy {
    position: absolute; left: 527px; top: 16px; width: 473px;
    color: var(--white); font-size: 15.3px; line-height: 18px;
  }
  .info-copy h1 {
    color: var(--lime); font-size: 37px; font-weight: 700; line-height: 40px;
    letter-spacing: -0.3px; margin-bottom: 0;
  }
  .info-copy p { text-align: justify; margin-bottom: 11px; }
  .info-copy .highlight { font-weight: 700; }
  .info-copy .accent { font-weight: 700; color: var(--lime); }

  .brand {
    position: absolute; left: 0; width: 354px; text-align: center;
    color: var(--white); font-weight: 400;
  }
  .brand-name { top: 618px; font-size: 35px; letter-spacing: 6px; }
  .brand-sub { top: 668px; font-size: 18px; letter-spacing: 4px; }

  .matching-line {
    position: absolute; right: 25px; top: 530px; width: 660px;
    text-align: right; color: var(--white);
    font-size: 18.5px; line-height: 24px; letter-spacing: 0.9px;
  }
  .location {
    position: absolute; right: 28px; top: 597px;
    font-family: "Kalam", cursive; color: var(--lime); font-size: 25px;
  }
  .phone {
    position: absolute; right: 28px; top: 636px;
    font-family: "Kalam", cursive; font-weight: 700; color: var(--white);
    font-size: 56px; letter-spacing: 9px; line-height: 70px;
  }
</style>
</head>
<body>
  <main class="flyer">
    <div class="stable-photo" role="img" aria-label="Photo of a chestnut horse looking out of a wooden stable door, with a paddock fence and trees beyond"></div>
    <div class="info-panel"></div>

    <svg class="wave" viewBox="0 0 1020 722" aria-hidden="true">
      <path d="M0 450 C150 408 300 408 500 468 C650 512 820 520 1020 462 L1020 722 L0 722 Z" fill="var(--forest)"/>
      <path d="M0 450 C150 408 300 408 500 468 C650 512 820 520 1020 462" fill="none" stroke="var(--lime)" stroke-width="3"/>
    </svg>

    <section class="info-copy">
      <h1>HORSE RIDING IS FUN!</h1>
      <p>Riders, particularly children, are taught not only skills on the horse, but skills that are integral to good horsemanship and ownership of horses.</p>
      <p class="highlight">We regularly host Ladies Days, Guest Instructors, 1 hour Trail Rides and Pony Ride Days!</p>
      <p>We teach people how to interact safely with, and care for horses so they develop a genuine love and respect for the animals and the sport.</p>
      <p class="accent">In addition to fundamental riding techniques including walk, trot, and canter, we teach our students:</p>
      <p>Grooming and Care of horses, Safety around horses, Balance and Co-Ordination, How to saddle up and care for Tack, Responsibility for equipment and horse, Confidence and Confidence Building for all Ages.</p>
      <p class="accent">Private and group lessons start at 5 years of age upwards.</p>
      <p>We recommend children 4 years and under partake in 15 minute pony rides, mainly due to their attention span!</p>
    </section>

    <div class="brand brand-name">FLEUR VALLON</div>
    <div class="brand brand-sub">RIDING SCHOOL</div>

    <p class="matching-line">At Fleur Vallon Riding School, Horses and ponies are carefully matched to suit each rider's experience, ability and confidence</p>
    <p class="location">Find us at Tamsin Rd, Coralbay</p>
    <p class="phone">0400 555 182</p>
  </main>
</body>
</html>
```